NGO... Kestrel Reading Path, Cambodia

require photo of banyan leaf one side and my info other side. I have an NGO doing village support work plus managing village schools in Cambodia. Require a simple square card with b/w design of leaf.
I am a volunteer organisation and provide small business opportunities for the local families.

Industry/Entity Type

Learning

Contact Information for Business Card

square card, banyan leaf design b/w

Font styles to use
Serif

```html
<!DOCTYPE html>
<html lang="en">
<head>
<meta charset="utf-8">
<title>Kestrel Reading Path – Business Card</title>
<link rel="stylesheet" href="https://fonts.googleapis.com/css2?family=Lora:wght@400;700&display=swap">
<style>
  :root {
    --card-bg: #000000;
    --ink: #ffffff;
    --leaf-light: #5a5a5a;
    --leaf-mid: #333333;
    --leaf-dark: #161616;
  }
  html, body {
    margin: 0;
    padding: 0;
    width: 1200px;
    height: 1200px;
    overflow: hidden;
    background: var(--card-bg);
  }
  .card {
    position: relative;
    width: 1200px;
    height: 1200px;
    background: var(--card-bg);
    color: var(--ink);
    font-family: "Lora", serif;
    overflow: hidden;
  }
  .leaf-art {
    position: absolute;
    left: 470px;
    top: 330px;
    width: 860px;
    height: 780px;
    border-radius: 55% 8% 60% 45% / 50% 10% 60% 50%;
    transform: rotate(-8deg);
    background: radial-gradient(ellipse at 60% 45%, var(--leaf-light) 0%, var(--leaf-mid) 45%, var(--leaf-dark) 85%);
    opacity: 0.85;
  }
  .line {
    position: absolute;
    left: 143px;
    margin: 0;
    line-height: 1;
    white-space: nowrap;
  }
  .name { top: 158px; font-size: 70px; }
  .name .first { font-weight: 700; }
  .name .last { font-weight: 400; }
  .role { top: 251px; font-size: 57px; font-weight: 400; }
  .address-1 { top: 464px; font-size: 57px; }
  .address-2 { top: 539px; font-size: 57px; }
  .phone-main { top: 670px; font-size: 84px; font-weight: 700; }
  .phone-alt { top: 771px; font-size: 57px; }
  .email { top: 918px; font-size: 57px; }
  .web { top: 996px; font-size: 57px; }
</style>
</head>
<body>
  <div class="card">
    <div class="leaf-art" role="img" aria-label="Black and white line drawing of a banyan leaf"></div>

    <h1 class="line name"><span class="first">KESTREL</span> <span class="last">READING PATH</span></h1>
    <p class="line role">MANAGER</p>

    <p class="line address-1">ABC-123, Place, City</p>
    <p class="line address-2">Country.</p>

    <p class="line phone-main">123-456-7890</p>
    <p class="line phone-alt">123-456-7890</p>

    <p class="line email">info@readingpath.org</p>
    <p class="line web">www.readingpath.org</p>
  </div>
</body>
</html>
```